Real Estate Company / Capital Needs Cards!

need business cards designed using the logos that were just designed by sketchhive.

Reason: per designers request deadline extended 1 day…thank you.

Target Market(s)

Investors and clients looking to purchase real estate or invest in the business.

Industry/Entity Type

Business

Requirements
Must have
• two designs - one for the real estate logo and one for the capital logo, similar but slightly different.
Nice to have
• something to make it pop (perhaps on the back)
Should not have
• much color

```html
<!DOCTYPE html>
<html lang="en">
<head>
<meta charset="utf-8">
<title>Norvale Real Estate – Business Cards</title>
<link rel="stylesheet" href="https://fonts.googleapis.com/css2?family=Cinzel:wght@400&family=Tinos:wght@400;700&display=swap">
<style>
  :root {
    --canvas: #e6e5e3;
    --card-dark: #2c2829;
    --card-light: #ffffff;
    --band-grey: #b9b9b9;
    --ink: #1f1d1e;
    --ink-soft: #8a8a8a;
    --mark-light: #dcdcdc;
    --mark-grey: #9c9c9c;
  }
  * { box-sizing: border-box; margin: 0; padding: 0; }
  html, body { width: 1200px; height: 900px; overflow: hidden; }
  body {
    background: var(--canvas);
    display: flex;
    align-items: center;
    justify-content: center;
    gap: 40px;
  }
  .card {
    position: relative;
    width: 540px;
    height: 309px;
    overflow: hidden;
    box-shadow: 0 6px 18px rgba(0,0,0,0.18);
  }
  /* Front */
  .card--front { background: var(--card-light); }
  .card__bands { position: absolute; inset: 0; width: 100%; height: 100%; }
  .contact {
    position: absolute;
    left: 38px;
    top: 26px;
    font-family: "Tinos", serif;
    color: var(--ink);
    z-index: 1;
  }
  .contact__name {
    font-weight: 700;
    font-size: 17px;
    letter-spacing: 0.5px;
    display: flex;
    align-items: center;
    gap: 6px;
  }
  .contact__name::before {
    content: "";
    width: 5px; height: 5px;
    background: var(--ink);
    border-radius: 50%;
  }
  .contact__role {
    font-size: 13px;
    color: var(--ink-soft);
    margin-left: 11px;
  }
  .contact__details {
    list-style: none;
    margin-top: 12px;
    font-size: 11.5px;
    font-weight: 700;
    line-height: 1.45;
  }
  .contact__details .label { color: var(--ink-soft); }
  .front-brand {
    position: absolute;
    right: 44px;
    top: 120px;
    display: flex;
    align-items: center;
    gap: 10px;
    font-family: "Tinos", serif;
    font-weight: 700;
    font-size: 26px;
    letter-spacing: 3px;
    color: var(--mark-grey);
  }
  .front-brand__square {
    width: 22px; height: 22px;
    background: var(--mark-grey);
    border-radius: 3px;
  }
  /* Back */
  .card--back {
    background: var(--card-dark);
    display: flex;
    flex-direction: column;
    align-items: center;
    justify-content: center;
    gap: 14px;
  }
  .back-brand__square {
    width: 64px; height: 64px;
    background: var(--mark-light);
    border-radius: 6px;
  }
  .back-brand__name,
  .back-brand__tag {
    font-family: "Cinzel", serif;
    font-weight: 400;
    color: var(--mark-light);
    text-align: center;
  }
  .back-brand__name { font-size: 38px; letter-spacing: 3px; line-height: 1; }
  .back-brand__tag { font-size: 14px; letter-spacing: 3px; margin-top: -8px; }
</style>
</head>
<body>
  <section class="card card--front" aria-label="Business card front">
    <svg class="card__bands" viewBox="0 0 540 309" preserveAspectRatio="none" aria-hidden="true">
      <path d="M0 188 C 140 232, 320 276, 540 296 L540 288 C 320 268, 140 224, 0 178 Z" fill="var(--band-grey)"/>
      <path d="M0 200 C 140 246, 320 290, 540 306 L540 309 L0 309 Z" fill="var(--card-dark)"/>
    </svg>
    <div class="contact">
      <p class="contact__name">YOUR NAME</p>
      <p class="contact__role">Company Position</p>
      <ul class="contact__details">
        <li>48 Alder Row Ste. 310</li>
        <li>Fairmont, Ca 90210</li>
        <li><span class="label">E:</span> youremail@norvalehomes.com</li>
        <li><span class="label">P:</span> 000-123-456</li>
        <li><span class="label">F:</span> 111-234-567</li>
      </ul>
    </div>
    <div class="front-brand">
      <span class="front-brand__square"></span>
      <span>NORVALE</span>
    </div>
  </section>

  <section class="card card--back" aria-label="Business card back">
    <span class="back-brand__square"></span>
    <p class="back-brand__name">NORVALE</p>
    <p class="back-brand__tag">REAL ESTATE</p>
  </section>
</body>
</html>
```